Business Cards

Business cards (double-sided) to be handed out to clients and potential clients, with contact details, logo .

Target Market(s)

Small to medium size businesses

Industry/Entity Type

Accountants

Contact Information for Business Card

Brightwater Ledger & Counsel Ltd

Colors

Designer to choose only greyscale colors for use in the design.

Requirements
Must have
• Name, Title, Address, Phone number, Email, Website
Nice to have
• Modern, clean lines, classy
Should not have
• Business cards to be double-sided. Form keeps reverting to single-sided.

```html
<!DOCTYPE html>
<html lang="en">
<head>
<meta charset="utf-8">
<title>Brightwater Ledger &amp; Counsel – Business Card</title>
<link rel="stylesheet" href="https://fonts.googleapis.com/css2?family=Montserrat:wght@400;500;700&display=swap">
<style>
  :root {
    --ink: #161616;
    --paper: #ffffff;
    --stage: #d6d6d6;
    --silver: #a9a9a9;
    --text-dark: #1c1c1c;
    --text-light: #f2f2f2;
  }
  * { box-sizing: border-box; margin: 0; padding: 0; }
  html, body {
    width: 1200px; height: 900px; overflow: hidden;
    background: var(--stage);
    font-family: "Montserrat", Arial, sans-serif;
  }
  .canvas { position: relative; width: 1200px; height: 900px; }

  .card {
    position: absolute; width: 600px; height: 343px;
    overflow: hidden;
    box-shadow: 0 6px 18px rgba(0,0,0,.25);
  }
  .card--front { left: 110px; top: 80px; background: var(--ink); }
  .card--back  { left: 490px; top: 477px; background: var(--paper); }

  .brand-name {
    font-weight: 500;
    text-transform: uppercase;
    letter-spacing: 3px;
    line-height: 1.25;
  }
  .card--front .brand-name {
    position: absolute; left: 0; right: 0; top: 50%;
    transform: translateY(-50%);
    text-align: center;
    color: var(--text-light);
    font-size: 30px;
  }
  .card--back .brand-name {
    position: absolute; left: 34px; top: 118px;
    color: var(--text-dark);
    font-size: 20px;
  }

  .holder { position: absolute; right: 34px; top: 34px; text-align: right; color: var(--text-dark); }
  .holder__name { font-weight: 700; font-size: 19px; letter-spacing: .5px; text-transform: uppercase; }
  .holder__title { font-size: 13px; margin-top: 4px; }

  .address {
    position: absolute; right: 34px; top: 138px;
    font-style: normal;
    text-align: right; font-size: 14px; line-height: 1.5; color: var(--text-dark);
  }

  .contacts {
    position: absolute; left: 34px; bottom: 58px;
    list-style: none; font-size: 14px; color: var(--text-dark);
  }
  .contacts li { display: flex; align-items: center; gap: 9px; line-height: 1.65; }
  .contacts svg { width: 13px; height: 13px; fill: var(--text-dark); flex: none; }

  .wave { position: absolute; inset: 0; width: 600px; height: 343px; }
  .wave__silver { fill: var(--silver); }
  .wave__ink { fill: var(--ink); }
</style>
</head>
<body>
<main class="canvas">

  <section class="card card--front" aria-label="Card front">
    <p class="brand-name">Brightwater<br>Ledger &amp; Counsel</p>
  </section>

  <section class="card card--back" aria-label="Card back">
    <svg class="wave" viewBox="0 0 600 343" aria-hidden="true">
      <path class="wave__silver" d="M0,302 C200,300 360,292 450,252 C520,220 560,207 600,202 L600,343 L0,343 Z"/>
      <path class="wave__ink" d="M0,313 C205,311 370,303 460,263 C528,231 565,219 600,215 L600,343 L0,343 Z"/>
    </svg>

    <p class="brand-name">Brightwater<br>Ledger &amp; Counsel</p>

    <div class="holder">
      <p class="holder__name">Daniel Hartwell</p>
      <p class="holder__title">Co-Founder</p>
    </div>

    <address class="address">
      42 Harbor Lane Suite 7<br>Westfield, NY 11720
    </address>

    <ul class="contacts">
      <li>
        <svg viewBox="0 0 24 24"><path d="M6.6 10.8a15.1 15.1 0 0 0 6.6 6.6l2.2-2.2c.3-.3.7-.4 1-.2 1.1.4 2.3.6 3.6.6.6 0 1 .4 1 1V20c0 .6-.4 1-1 1A17 17 0 0 1 3 4c0-.6.4-1 1-1h3.5c.6 0 1 .4 1 1 0 1.3.2 2.5.6 3.6.1.3 0 .7-.2 1z"/></svg>
        555-214-3098
      </li>
      <li>
        <svg viewBox="0 0 24 24"><path d="M2 5h20v14H2z M2 5l10 8 10-8" fill="none" stroke="#1c1c1c" stroke-width="2"/></svg>
        info@brightwaterledger.com
      </li>
      <li>
        <svg viewBox="0 0 24 24"><circle cx="12" cy="12" r="10"/></svg>
        www.brightwaterledger.com
      </li>
    </ul>
  </section>

</main>
</body>
</html>
```